Interior Design & consultancy firm requires a new business card design that is a little bit funky bu

Kestrova Design Services is a leading strategic design practice specialising in the development and implementation of strategies and design solutions for commercial workplaces across a wide variety of industries.

The company has over twenty years experience in the strategic design, development and construction of innovative and efficient workplace environments for the commercial, corporate and industrial sectors.

We believe good design and efficient workspaces can transform companies, improve people’s lives and increase productivity.

Target Market(s)

My clients are mainly Government or corporate clients wanting to create a statement with their office fitout & new furniture that reflects their corporate identity

Industry/Entity Type

Construction

Font styles to use
Sans Serif

Colors
add136

Requirements
Must have
• The business card must be easy to read, simple & highlight my name & mobile phone number
Should not have
• I do not want the card to be fussy, feature too many colours or look to busy.

```html
<!DOCTYPE html>
<html lang="en">
<head>
<meta charset="utf-8">
<title>Kestrova Design Services – Business Card</title>
<link href="https://fonts.googleapis.com/css2?family=Lato:wght@300;400&display=swap" rel="stylesheet">
<style>
  :root {
    --canvas-bg: #d9d9d7;
    --card-bg: #353431;
    --ink-light: #e6e6e4;
    --ink-soft: #b9b8b4;
    --ink-faint: #45443f;
    --rule: #8f8e8a;
  }
  * { margin: 0; padding: 0; box-sizing: border-box; }
  html, body {
    width: 1200px;
    height: 1200px;
    overflow: hidden;
    background: var(--canvas-bg);
    font-family: "Lato", "Helvetica Neue", Arial, sans-serif;
  }
  .sheet {
    width: 1200px;
    height: 1200px;
    display: flex;
    flex-direction: column;
    align-items: center;
    justify-content: center;
    gap: 60px;
  }
  .card {
    position: relative;
    width: 900px;
    height: 500px;
    background: var(--card-bg);
    color: var(--ink-light);
    box-shadow: 0 10px 28px rgba(0,0,0,0.18);
  }

  /* Front */
  .brand {
    position: absolute;
    display: flex;
    align-items: center;
    gap: 16px;
    font-weight: 300;
    letter-spacing: 0.12em;
    text-transform: uppercase;
    white-space: nowrap;
  }
  .brand-mark {
    width: 22px;
    height: 22px;
    border: 2px solid currentColor;
  }
  .card-front .brand {
    left: 50%;
    top: 50%;
    transform: translate(-50%, -50%);
    font-size: 34px;
    color: var(--ink-light);
  }

  /* Back */
  .card-back .brand-faint {
    left: 50%;
    top: 50%;
    transform: translate(-50%, -50%);
    font-size: 28px;
    color: var(--ink-faint);
  }
  .holder {
    position: absolute;
    right: 60px;
    top: 96px;
    width: 330px;
  }
  .holder-name {
    font-size: 30px;
    font-weight: 400;
    letter-spacing: 0.06em;
    color: var(--ink-light);
    padding-bottom: 8px;
    border-bottom: 1px solid var(--rule);
  }
  .holder-role {
    margin-top: 6px;
    font-size: 13px;
    letter-spacing: 0.08em;
    color: var(--ink-soft);
  }
  .contact {
    position: absolute;
    left: 60px;
    bottom: 80px;
    list-style: none;
    font-size: 19px;
    font-weight: 400;
    letter-spacing: 0.06em;
    line-height: 2;
    color: var(--ink-light);
  }
</style>
</head>
<body>
  <main class="sheet">
    <section class="card card-front" aria-label="Card front">
      <div class="brand">
        <span class="brand-mark"></span>
        <span class="brand-name">Kestrova Design Services</span>
      </div>
    </section>

    <section class="card card-back" aria-label="Card back">
      <div class="brand brand-faint" aria-hidden="true">
        <span class="brand-name">Kestrova Design Services</span>
      </div>
      <div class="holder">
        <p class="holder-name">Tessa Lindqvist.</p>
        <p class="holder-role">Director</p>
      </div>
      <ul class="contact">
        <li>M: 0412 587 230</li>
        <li>P: 0255501734</li>
        <li>E: tessalindqvist@kestrovadesign.com</li>
      </ul>
    </section>
  </main>
</body>
</html>
```